Welcome to the neighborhood...here's what we have to offer

Would like to send a 2 sided post card to new homeowners Congratulating them on their move or welcoming them to the neighborhood. In the post card we will inform them that Corvalt VInyl Corporation offers vinyl railing systems, vinyl fence systems and aluminum fence systems. Railing Systems can be on one side of the card and fences on the other. We offer high quality products with professional installation. We accept Paxo, CoinPlate, Brightlane, KoruPay, Check, Cash and have financing available. Have included a few pictures of fences and several picture of railing systems to choose from.
A note to be included..For every fence installed in South Central Pennsylvania we donate 10.00 to an Animal Welfare organization

Our website address is www.corvaltvinylfence.example

```html
<!DOCTYPE html>
<html lang="en">
<head>
<meta charset="utf-8">
<title>Good Fences Make Good Neighbors</title>
<link rel="stylesheet" href="https://fonts.googleapis.com/css2?family=Montserrat:ital,wght@0,700;0,800;1,800;1,900&display=swap">
<style>
  :root {
    --white: #ffffff;
    --shadow: #5a5a56;
    --ink: #141414;
    --muted: #4a4945;
    --accent: #d8262c;
    --bg-top: #2c2a26;
    --fence: #aaa699;
    --fence-low: #8f8c80;
    --planting: #3c4630;
    --ground: #2a2622;
    --sidewalk: #d4d2cc;
    --deck-sky: #e6e8ea;
    --deck-house: #c9ccd0;
    --deck-floor: #5e6268;
  }
  * { margin: 0; padding: 0; box-sizing: border-box; }
  html, body { width: 1200px; height: 930px; overflow: hidden; background: var(--white); }
  .card {
    position: relative;
    width: 1200px;
    height: 930px;
    overflow: hidden;
    font-family: "Montserrat", Arial, sans-serif;
  }
  .scene-photo {
    position: absolute;
    inset: 0;
    background:
      radial-gradient(ellipse 560px 420px at 0% 100%, var(--sidewalk) 0%, var(--sidewalk) 62%, rgba(212,210,204,0) 100%),
      linear-gradient(180deg,
        var(--bg-top) 0%, var(--bg-top) 11%,
        var(--fence) 14%, var(--fence) 42%,
        var(--fence-low) 58%, var(--planting) 68%,
        var(--ground) 82%, var(--ground) 100%);
  }
  .headline {
    position: absolute;
    inset: 0;
    color: var(--white);
    font-weight: 900;
    font-style: italic;
    font-size: 96px;
    line-height: 1;
    letter-spacing: 1px;
    text-shadow: 7px 7px 0 var(--shadow);
  }
  .headline span { position: absolute; white-space: nowrap; }
  .headline .line-1 { left: 222px; top: 348px; }
  .headline .line-2 { left: 272px; top: 456px; }
  .headline .line-3 { left: 330px; top: 550px; }
  .tagline {
    position: absolute;
    right: 476px;
    top: 672px;
    text-align: right;
    color: var(--white);
    font-weight: 800;
    font-style: italic;
    font-size: 27px;
    line-height: 43px;
    letter-spacing: 1.5px;
    text-shadow: 3px 3px 0 var(--shadow);
  }
  .deck-photo {
    position: absolute;
    left: 737px;
    top: 681px;
    width: 268px;
    height: 200px;
    background: linear-gradient(180deg, var(--deck-sky) 0%, var(--deck-house) 55%, var(--deck-floor) 85%, var(--planting) 100%);
  }
  .contact {
    position: absolute;
    left: 48px;
    top: 680px;
    color: var(--muted);
    font-weight: 800;
    font-size: 15px;
    line-height: 26px;
  }
  .brand {
    position: absolute;
    left: 48px;
    top: 834px;
    display: flex;
    align-items: center;
    gap: 10px;
    color: var(--ink);
    font-weight: 800;
    font-size: 31px;
    letter-spacing: 1px;
  }
  .brand-mark { width: 18px; height: 18px; background: var(--accent); }
  .brand-division {
    position: absolute;
    left: 48px;
    top: 876px;
    color: var(--muted);
    font-weight: 800;
    font-size: 14px;
  }
</style>
</head>
<body>
  <div class="card">
    <div class="scene-photo" role="img" aria-label="Photograph of a tall tan vinyl privacy fence with shrubs, mulch bed, bollard lights and a concrete sidewalk"></div>

    <h1 class="headline">
      <span class="line-1">GOOD FENCES</span>
      <span class="line-2">MAKE GOOD</span>
      <span class="line-3">NEIGHBORS.</span>
    </h1>

    <p class="tagline">And good railings<br>make happy<br>insurance<br>agents.</p>

    <div class="deck-photo" role="img" aria-label="Photograph of a white vinyl railing on a raised deck beside a white house"></div>

    <div class="contact">
      <p>Welcome home! Call • 717-555-0142</p>
      <p>www.corvaltvinylfence.example</p>
      <p>Paxo, CoinPlate, Brightlane, KoruPay,</p>
      <p>Check &amp; Cash • Financing Available</p>
      <p>$10 per fence to Animal Welfare</p>
    </div>

    <div class="brand">
      <span class="brand-name">Corvalt Fence Railing</span>
      <span class="brand-mark"></span>
    </div>
    <p class="brand-division">A Division of Corvalt Vinyl Corporation</p>
  </div>
</body>
</html>
```